Peptide Weight Loss Trifold

A trifold to market peptide weight loss injections. We are different than other clinics, in that we offer a three step approach to effortlessly lose weight and keep it off.

The peptides used are Semaglutide and AOD9604, both proven to . We also have Vitalis Core, a product that heals the gut biome and brain hormone response to weight loss. These three items stacked together is what sets us apart from other clinics. Both peptides are approved by the NHB for weight loss.

We also compound our peptides so they are much cheaper than the commercial Semaglutide also known as Lunavex, and Trelmo. These two commercial peptides from big pharma, each run about 1200.00 per month. Our compounded peptides are a fraction of that cost.
AOD9604....(Anti Obesity Drug)
Patients are losing as much weight as if they had bariatric surgery. 3-5 pounds per week.

If your are like 85% of dieters, its not your first time trying to get healthy and lose weight.
Join thousands of folks pushing the past plateaus and kill the cravings without starving via Quarlin MD's 16-Week program.
Five Star reviews.
"I have been on Semaglutide for one month. I guess the numbers are the crucial part of all semaglutide reviews. That’s it. I have dropped 16lbs. One of the things I have truly come to appreciate is that Sem will limit your appetite. " Marisol
"I’ve lost 13.5 pounds in a month, and I can’t even tell how it happened. The interesting part is that I don’t want to eat sweets anymore. I just want to eat less, I eat small portions while losing weight and enjoy my life." Tansy47
" I’ve been on the double peptide plan for a month and have dropped 20 pounds, despite not exercising. I’m delighted to see these figures change." Wendell
"Semaglutide worked for me. 10 out of 10." Gus

Hunger pangs! The primary roadblock to weight loss. With semaglutide, hunger pangs are a thing of the past. Semaglutide....changing the game!

Benefits of Semaglutide:
Reduces hunger pangs
Makes you feel fuller longer
Reduces food cravings
Reduces cardiovascular risk factors
Improves insulin sensitivity
Convenient once-weekly dosing

Is Semaglutide Safe?
Semaglutide is a safe, NHB-approved medication with minimal side effects.

Benefits of AOD 9604
Fat doesn’t stand a chance against this naturally powerful peptide, whose impressive fat-fighting abilities can provide the following benefits, such as:

Reduces body fat
Increases calorie burn
Triggers fat release>
Boosts your metabolism
Prevents non-fatty foods from turning into body fat
Doesn’t increase your appetite

A weight loss breakthrough.
Recent scientific discoveries offer insight into how our metabolism and hormones change over time — and how that impacts whether we’ll gain or lose weight. It comes down to the relationship between our brains and our guts.

A new family of medications called GLP-1s address these biological factors head-on. THE TRUTH IS...
It's not about willpower.
It's biology.
Up to 70% of weight gain is linked to genetics. On top of that, other health conditions and medications can make weight loss even more difficult.

And the environment we live in can influence our access to affordable and reliable healthcare and nutrition.

Peptide GLP-1s fight back against these genetic, biological, and environmental factors that prevent weight loss.
244 genes linked to obesity
BOOSTING YOUR BODY'S NATURAL ABILITIES
How GLP-1s Work
WHAT

A naturally occurring hormone
GLP-1 is naturally released by the gut in response to food.

HOW

An extra boost for your system
The effects include increasing insulin release from the pancreas, slowing down stomach emptying, and targeting receptors in the brain that cause appetite reduction.

RESULT

A more efficient weight loss outcome
This results in a sensation of satiety, or fullness, lasting much longer than possible with natural GLP-1 hormone levels.
Other medications
Your Brightpath Clinician may determine that another medication or a combination of medications might work best for your medical history and biology. They will do a careful review of your specific case to ensure you’re getting an effective medication that meets your needs.

You can learn more about different medications, common side effects, and their results and costs, by call us today for a free consultation at 480-317-SLIM

Here is a layout that I woukd like inside on the bottom half

Went on vacation/holiday

Target Market(s)

anyone with a BMI over28

Industry/Entity Type

medical weight loss

Requirements
Must have
• call to action
Nice to have
• include 5 star review
Should not have
• too many words

```html
<!DOCTYPE html>
<html lang="en">
<head>
<meta charset="utf-8">
<title>Peptide Weight Loss Trifold</title>
<link href="https://fonts.googleapis.com/css2?family=Open+Sans:wght@400;600;700;800&display=swap" rel="stylesheet">
<style>
:root{
  --green:#6aa533;
  --green-dark:#4f8a26;
  --green-light:#8cc63f;
  --orange:#f0842c;
  --orange-light:#f6a04d;
  --ink:#3d3d3d;
  --muted:#777;
  --paper:#fbfbfa;
  --stage:#e4e4e4;
  --photo-skin:#d9c2ad;
  --photo-room:#ece6dc;
}
*{box-sizing:border-box;margin:0;padding:0}
html,body{width:1080px;height:1200px;overflow:hidden;background:var(--stage)}
body{font-family:"Open Sans",sans-serif;color:var(--ink);position:relative}
.trifold{position:absolute;left:20px;width:1040px;height:560px;display:grid;grid-template-columns:repeat(3,1fr);background:var(--paper);box-shadow:0 4px 14px rgba(0,0,0,.15)}
.trifold--outside{top:24px}
.trifold--inside{top:616px}
.panel{position:relative;overflow:hidden;border-right:1px solid rgba(0,0,0,.06)}
.panel:last-child{border-right:0}
.photo{position:absolute;background:linear-gradient(135deg,var(--photo-room),var(--photo-skin))}
.shape{position:absolute;left:0;width:100%}
.pill{display:inline-block;background:linear-gradient(var(--orange-light),var(--orange));color:#fff;font-weight:700;border-radius:20px;text-transform:uppercase}
.body-copy{font-size:8px;line-height:1.4;text-align:justify}
.body-copy p+p{margin-top:6px}

/* outside left */
.peptides .photo{top:0;left:0;right:0;height:200px}
.peptides .body-copy{position:absolute;top:212px;left:24px;right:24px}
.peptides .cta{position:absolute;left:0;right:0;bottom:22px;text-align:center;color:#fff}
.cta__lead{font-size:8.5px;line-height:1.4;padding:0 50px}
.cta__rule{width:40px;height:1px;background:#fff;margin:6px auto}
.cta__free{font-size:13px;font-weight:700}
.cta__phone{margin-top:8px;font-size:21px;padding:6px 26px;letter-spacing:.5px}

/* outside middle */
.reviews__title{position:absolute;top:40px;left:0;right:0;text-align:center}
.reviews__title .pill{font-size:12px;padding:5px 22px}
.review-list{position:absolute;top:82px;left:22px;right:22px}
.review{border:1px solid var(--green-light);border-radius:10px;padding:6px 10px 5px;text-align:center;margin-bottom:8px}
.review__quote{font-size:7.6px;line-height:1.4}
.review__name{color:var(--orange);font-size:8px;font-weight:700;margin-top:2px}
.review__stars{color:var(--orange);font-size:11px;letter-spacing:2px;line-height:1.1}
.contact{position:absolute;left:20px;right:20px;bottom:16px;color:#fff;display:grid;grid-template-columns:1.3fr 1fr;row-gap:10px;column-gap:10px}
.contact h4{font-size:10px;font-weight:700}
.contact p{font-size:7.5px;line-height:1.4}
.contact div+div{border-left:1px solid rgba(255,255,255,.6);padding-left:10px}
.contact div:nth-child(3){border-left:0;padding-left:0}

/* outside right (cover) */
.brand{position:absolute;top:26px;left:0;right:0;text-align:center}
.brand__name{display:inline-flex;align-items:center;gap:8px;color:var(--green);font-size:24px;font-weight:700}
.brand__mark{width:14px;height:14px;border-radius:50%;background:var(--green)}
.cover .photo{top:88px;left:40px;right:0;height:240px}
.cover__headline{position:absolute;top:340px;left:24px;right:20px;text-align:center;color:var(--green);font-size:17px;font-weight:800;line-height:1.2}
.cover__sub{position:absolute;top:410px;left:30px;right:30px;text-align:center;font-size:8.5px;font-weight:600;line-height:1.4}
.cover__web{position:absolute;bottom:16px;right:24px;color:#fff;font-size:9px;letter-spacing:1px}

/* inside left */
.hunger .photo{top:0;left:0;right:0;height:250px}
.hunger__copy{position:absolute;top:258px;left:22px;right:22px;color:#fff}
.hunger__copy h2{font-size:16px;font-weight:800;margin-bottom:4px}
.hunger__copy h3{font-size:14px;font-weight:800;margin:8px 0 4px}
.hunger__copy .body-copy{font-size:7.6px}

/* inside middle */
.benefits__photo{position:absolute;top:22px;left:50%;width:170px;height:170px;margin-left:-85px;border-radius:50%;border:5px solid var(--green);background:linear-gradient(135deg,#9fcf6a,var(--photo-skin))}
.benefits__copy{position:absolute;top:210px;left:30px;right:22px}
.benefits__copy h3{color:var(--orange);font-size:12.5px;font-weight:800;margin:8px 0 4px}
.benefits__copy h3:first-child{margin-top:0}
.benefits__copy p{font-size:8px;line-height:1.4}
.ticks{list-style:none}
.ticks li{position:relative;padding-left:16px;font-size:8px;line-height:1.55}
.ticks li::before{content:"";position:absolute;left:0;top:2.5px;width:9px;height:9px;border-radius:50%;background:var(--green)}
.ticks li::after{content:"";position:absolute;left:3px;top:4.5px;width:2px;height:4px;border:solid #fff;border-width:0 1.2px 1.2px 0;transform:rotate(45deg)}

/* inside right */
.glp__head{position:absolute;top:22px;left:0;right:0;text-align:center;color:#fff}
.glp__head h2{font-size:12.5px;font-weight:600;line-height:1.3;text-transform:uppercase}
.glp__head .pill{font-size:11px;padding:4px 18px;margin-top:6px;text-transform:none}
.steps{position:absolute;top:100px;left:18px;right:22px;color:#fff}
.step{display:grid;grid-template-columns:24px 1fr;column-gap:8px;margin-bottom:10px}
.step__icon{width:22px;height:22px;border-radius:50%;border:1px dashed rgba(255,255,255,.85);position:relative}
.step__icon::after{content:"";position:absolute;left:7px;top:7px;width:6px;height:6px;border-radius:50%;background:rgba(255,255,255,.85)}
.step h4{font-size:9px;font-weight:800}
.step p{font-size:7.5px;line-height:1.4}
.glp .photo{left:0;right:0;bottom:0;height:170px}
</style>
</head>
<body>

<section class="trifold trifold--outside" aria-label="Trifold outside">
  <!-- Peptides panel -->
  <article class="panel peptides">
    <div class="photo" role="img" aria-label="Photo of a smiling dark-haired woman in a bright room"></div>
    <svg class="shape" style="top:0;height:60px" viewBox="0 0 347 60" preserveAspectRatio="none"><path d="M0 0H347V0C250 6 120 30 0 60Z" fill="var(--green)"/></svg>
    <div class="body-copy">
      <p>The peptides used are Semaglutide and AOD9604, both proven to . We also have Vitalis Core, a product that heals the gut biome and brain hormone response to weight loss. These three items stacked together is what sets us apart from other clinics. Both peptides are approved by the NHB for weight loss.</p>
      <p>We also compound our peptides so they are much cheaper than the commercial Semaglutide also known as Lunavex, and Trelmo. These two commercial peptides from big pharma, each run about 1200.00 per month. Our compounded peptides are a fraction of that cost. AOD9604....(Anti Obesity Drug)</p>
      <p>Patients are losing as much weight as if they had bariatric surgery. 3-5 pounds per week.</p>
    </div>
    <svg class="shape" style="bottom:0;height:200px" viewBox="0 0 347 200" preserveAspectRatio="none">
      <path d="M0 40C120 30 260 10 347 0V200H0Z" fill="var(--orange)"/>
      <path d="M0 52C120 40 260 22 347 12V200H0Z" fill="var(--green)"/>
    </svg>
    <div class="cta">
      <p class="cta__lead">You can learn more about different medications, common side effects, and their results and costs.</p>
      <div class="cta__rule"></div>
      <p class="cta__lead">By call us today for a</p>
      <p class="cta__free">Free consultation at</p>
      <span class="pill cta__phone">480-317-SLIM</span>
    </div>
  </article>

  <!-- Reviews panel -->
  <article class="panel reviews">
    <svg class="shape" style="top:0;height:60px" viewBox="0 0 347 60" preserveAspectRatio="none"><path d="M0 0H347V30C250 10 120 14 0 40Z" fill="var(--green)"/></svg>
    <div class="reviews__title"><span class="pill">Our Reviews</span></div>
    <div class="review-list">
      <div class="review">
        <p class="review__quote">I have been on Semaglutide for one month. I guess the numbers are the crucial part of all semaglutide reviews. That’s it. I have dropped 16lbs. One of the things I have truly come to appreciate is that Sem will limit your appetite.</p>
        <p class="review__name">- Marisol</p>
        <p class="review__stars">★★★★★</p>
      </div>
      <div class="review">
        <p class="review__quote">I’ve lost 13.5 pounds in a month, and I can’t even tell how it happened. The interesting part is that I don’t want to eat sweets anymore. I just want to eat less, I eat small portions while losing weight and enjoy my life.</p>
        <p class="review__name">- Tansy47</p>
        <p class="review__stars">★★★★★</p>
      </div>
      <div class="review">
        <p class="review__quote">I’ve been on the double peptide plan for a month and have dropped 20 pounds, despite not exercising. I’m delighted to see these figures change.</p>
        <p class="review__name">- Wendell</p>
        <p class="review__stars">★★★★★</p>
      </div>
      <div class="review">
        <p class="review__quote">Semaglutide worked for me. 10 out of 10.</p>
        <p class="review__name">- Gus</p>
        <p class="review__stars">★★★★★</p>
      </div>
    </div>
    <svg class="shape" style="bottom:0;height:120px" viewBox="0 0 347 120" preserveAspectRatio="none"><path d="M0 0C120 22 240 22 347 6V120H0Z" fill="var(--green)"/></svg>
    <div class="contact">
      <div><h4>Address :</h4><p>Quarlin MD - Harbor Office<br>2740 N Alder Crest Suite 210<br>Fenwick , Arizona 85099</p></div>
      <div><h4>Website :</h4><p>www.quarlinmd.com</p></div>
      <div><h4>Phone :</h4><p>(480) 555-0142</p></div>
      <div><h4>Fax :</h4><p>(480) 555-0178</p></div>
    </div>
  </article>

  <!-- Cover panel -->
  <article class="panel cover">
    <div class="brand">
      <div class="brand__name"><span class="brand__mark"></span>Quarlin MD</div>
    </div>
    <svg class="shape" style="top:66px;height:30px" viewBox="0 0 347 30" preserveAspectRatio="none"><path d="M20 26C120 4 240 2 330 8" fill="none" stroke="var(--green-light)" stroke-width="3"/></svg>
    <div class="photo" role="img" aria-label="Photo of a smiling woman in sportswear measuring her waist with a tape"></div>
    <svg class="shape" style="top:290px;height:50px" viewBox="0 0 347 50" preserveAspectRatio="none"><path d="M0 50C120 40 250 20 347 0V50Z" fill="var(--paper)"/></svg>
    <h1 class="cover__headline">Hormone Imbalance, Thyroid Problems or Just Preparing for Menopause</h1>
    <p class="cover__sub">Specializing in Bio-Identical Hormone Replacement Therapy, Thyroid Optimization, and Medically assisted Weight Loss.</p>
    <svg class="shape" style="bottom:0;height:100px" viewBox="0 0 347 100" preserveAspectRatio="none">
      <path d="M0 40C130 36 260 14 347 0V100H0Z" fill="#d6d6d6"/>
      <path d="M0 50C130 46 260 26 347 12V100H0Z" fill="var(--green)"/>
    </svg>
    <p class="cover__web">www.quarlinmd.com</p>
  </article>
</section>

<section class="trifold trifold--inside" aria-label="Trifold inside">
  <!-- Hunger panel -->
  <article class="panel hunger">
    <div class="photo" role="img" aria-label="Photo of a smiling young woman in a sports top measuring her waist"></div>
    <svg class="shape" style="top:220px;height:340px" viewBox="0 0 347 340" preserveAspectRatio="none"><path d="M0 40C120 30 250 16 347 0V340H0Z" fill="var(--green)"/></svg>
    <div class="hunger__copy">
      <h2>Hunger pangs!</h2>
      <p class="body-copy">The primary roadblock to weight loss. With semaglutide, hunger pangs are a thing of the past. Semaglutide....changing the game!</p>
      <p class="body-copy" style="margin-top:6px">If your are like 85% of dieters, its not your first time trying to get healthy and lose weight. Join thousands of folks pushing the past plateaus and kill the cravings without starving via Quarlin MD's 16-Week program.</p>
      <h3>A weight loss breakthrough.</h3>
      <p class="body-copy">Recent scientific discoveries offer insight into how our metabolism and hormones change over time — and how that impacts whether we’ll gain or lose weight. It comes down to the relationship between our brains and our guts. A new family of medications called GLP-1s address these biological factors head-on. THE TRUTH IS... It's not about willpower. It's biology. Up to 70% of weight gain is linked to genetics. On top of that, other health conditions and medications can make weight loss even more difficult. And the environment we live in can influence our access to affordable and reliable healthcare and nutrition. Peptide GLP-1s fight back against these genetic, biological, and environmental factors that prevent weight loss. 244 genes linked to obesity</p>
    </div>
  </article>

  <!-- Benefits panel -->
  <article class="panel benefits">
    <div class="benefits__photo" role="img" aria-label="Round photo of a slim waist wrapped in a yellow measuring tape"></div>
    <div class="benefits__copy">
      <h3>Benefits of Semaglutide :</h3>
      <ul class="ticks">
        <li>Reduces hunger pangs</li>
        <li>Makes you feel fuller longer</li>
        <li>Reduces food cravings</li>
        <li>Reduces cardiovascular risk factors</li>
        <li>Improves insulin sensitivity</li>
        <li>Convenient once-weekly dosing</li>
      </ul>
      <h3>Is Semaglutide Safe?</h3>
      <p>Semaglutide is a safe, NHB-approved medication with minimal side effects.</p>
      <h3>Benefits of AOD :</h3>
      <p>Fat doesn’t stand a chance against this naturally powerful peptide, whose impressive fat-fighting abilities can provide the following benefits, such as:</p>
      <ul class="ticks" style="margin-top:4px">
        <li>Reduces body fat</li>
        <li>Increases calorie burn</li>
        <li>Triggers fat release&gt;</li>
        <li>Boosts your metabolism</li>
        <li>Prevents non-fatty foods from turning into body fat</li>
        <li>Doesn’t increase your appetite</li>
      </ul>
    </div>
  </article>

  <!-- GLP-1 panel -->
  <article class="panel glp">
    <svg class="shape" style="top:0;height:420px" viewBox="0 0 347 420" preserveAspectRatio="none"><path d="M0 0H347V370C240 380 120 400 0 420Z" fill="var(--green)"/></svg>
    <div class="glp__head">
      <h2>Boosting your body's<br>natural abilities</h2>
      <span class="pill">How GLP-1s Work</span>
    </div>
    <div class="steps">
      <div class="step"><span class="step__icon"></span><div><h4>WHAT</h4><p>A naturally occurring hormone. GLP-1 is naturally released by the gut in response to food.</p></div></div>
      <div class="step"><span class="step__icon"></span><div><h4>HOW</h4><p>An extra boost for your system. The effects include increasing insulin release from the pancreas, slowing down stomach emptying, and targeting receptors in the brain that cause appetite reduction.</p></div></div>
      <div class="step"><span class="step__icon"></span><div><h4>RESULT</h4><p>A more efficient weight loss outcome. This results in a sensation of satiety, or fullness, lasting much longer than possible with natural GLP-1 hormone levels. Other medications: Your Brightpath Clinician may determine that another medication or a combination of medications might work best for your medical history and biology. They will do a careful review of your specific case to ensure you’re getting an effective medication that meets your needs.</p></div></div>
    </div>
    <div class="photo" role="img" aria-label="Photo of a clinician measuring a smiling patient's waist in a clinic"></div>
    <svg class="shape" style="bottom:150px;height:40px" viewBox="0 0 347 40" preserveAspectRatio="none"><path d="M0 40C120 20 240 8 347 0V0H0Z" fill="var(--green)"/></svg>
  </article>
</section>

</body>
</html>
```